Zestro Design Award - $10,000 tablet app design contest, Retail Catalogue Category

Zestro is a marketplace for Slatebook App Templates (similar to PageForge templates). We want you to design an app template for sale in our marketplace which targets Retail Catalogue Apps (Slatebook Apps that are created for Product Catalogues. For example: paint, clothing… etc).

It’s up to you to create pages or features for the App Template that you think are appropriate. Creativity will be rewarded! Here are some example pages or features that you could create:

• Welcome page
• Features
• Product pages
• Product details
• Share products on Friendlane
• Maps – store locations or events
• Social media integration
• Animations and video

Your design should be Vibrant, Engaging and Contemporary. If you have an Slatebook, download Zestro Lens and download template examples in the download tab.

Your entry must include:
• A brief description of your template
• Preview images of all pages of your template

Attached to this project are free templates to help you get started with your design. We have included:
1. A free portfolio template for designers/photographers
2. Icons and artwork to use in your template
3. Blank pages template
4. Form template
5. Video ad template

If you are selected as a finalist you will be required to submit an .zproject file containing:
• Your LayoutPro source files
• Preview images of your template
• All creative / stock assets used in the template (animations, video etc.)
• A text file with instructions on how to update the template
• A metadata .txt file containing template details and your information

How to enter:
1. Register at Marketplace and view the instructions under the welcome message https://market.zestrobase.example/welcome
2. Download Zestro Builder: https://help.zestrobase.example/entries/48175209-zestro-builder
3. Use the free templates provided in this brief to create your designs and submit to ArtPluvia
Updates

Project Deadline Extended
Reason: Due to the Christmas break we are extending the deadline of our competition. Thank you for time and effort - I will be providing feedback over the next couple of days! Best wishes, Melody

Hi All,

I have received many screenshots with some great designs! I just wanted to clarify that you are designing Zestro app templates including Zestro features and not just page designs?

Read Tips for First Time Zestroers to guide you through the template creation process

Before you start designing templates for Zestro Bazaar

·       Read the Quality Standards

·       Read the Copyright Information 

·       Use the Template Quality Checklist to ensure your template follows our guidelines. 

What should my project file contain?

·       A folder containing your source files, e.g. LayoutPro. This must be named Source.

·       The Zestro content files. This must be named Bundle.

·       Instructions, explaining to a customer how to use your template.

Best wishes,

Melody

Project Deadline Extended
Reason: We are extending the competition by 7 days to give you more time!

Project Deadline Extended
Reason: Due to the lack of submissions to this category we are extending the deadline by 10 days Please let us know if you would like further information on this contest. Best wishes, Melody

Target Market(s)

Entrepreneurs who wish to create Slatebook Apps by using our App design templates.

Industry/Entity Type

Store

Requirements
Must have
• You will need Zestro Builder to open the .zproject files attached to this brief. Get it here: https://help.zestrobase.example/entries/48175209-zestro-builder
Should not have
• • Low quality, fuzzy or blurry images
• Any stock images or content which you do not own the rights to
• Any material which could be considered inappropriate or offensive

```html
<!DOCTYPE html>
<html lang="en">
<head>
<meta charset="utf-8">
<title>Zestro Retail Catalogue – Tablet App Template</title>
<link rel="stylesheet" href="https://fonts.googleapis.com/css2?family=Arimo:wght@400;700&display=swap">
<style>
  :root {
    --canvas: #f2f2f2;
    --screen: #e9e9e9;
    --white: #ffffff;
    --ink-grey: #5a5a5a;
    --icon-grey: #9a9a9a;
    --add-green: #5bb531;
    --green-a: #8dc63f; --green-b: #39b54a;
    --blue-a: #29abe2;  --blue-b: #0e6bb4;
    --red-a: #ec1c24;   --red-b: #b8232a;
    --yellow-a: #f9ed1f; --yellow-b: #f9a13a;
    --pink-a: #f27aa8;  --pink-b: #e3147c;
    --pale-a: #ffffff;  --pale-b: #e2e2e2;
    --orange-a: #f7941d; --orange-b: #f05a24;
    --brown-a: #a87d55; --brown-b: #8c6543;
    --teal-a: #1fbf9f;  --teal-b: #0aa29e;
    --navy-a: #2e3192;  --navy-b: #262262;
  }
  * { box-sizing: border-box; margin: 0; padding: 0; }
  html, body { width: 1200px; height: 800px; overflow: hidden; }
  body {
    background: var(--canvas);
    font-family: "Arimo", Arial, sans-serif;
    position: relative;
  }
  .sprites { position: absolute; width: 0; height: 0; }

  .screen {
    position: absolute;
    background: linear-gradient(180deg, #f0f0f0, var(--screen));
    box-shadow: 0 0 0 1px #d8d8d8;
  }
  .screen--home     { left: 480px; top: 66px;  width: 610px; height: 399px; }
  .screen--ringtone { left: 47px;  top: 294px; width: 313px; height: 204px; }
  .screen--wallpaper{ left: 47px;  top: 558px; width: 313px; height: 206px; }
  .screen--catalogue{ left: 438px; top: 558px; width: 312px; height: 206px; }
  .screen--games    { left: 829px; top: 558px; width: 314px; height: 206px; }

  .tile {
    position: absolute;
    color: var(--white);
    font-weight: 700;
    display: flex;
  }
  .tile svg { margin: auto; }
  .tile--green  { background: linear-gradient(90deg, var(--green-a), var(--green-b)); }
  .tile--blue   { background: linear-gradient(90deg, var(--blue-a), var(--blue-b)); }
  .tile--red    { background: linear-gradient(90deg, var(--red-a), var(--red-b)); }
  .tile--yellow { background: linear-gradient(90deg, var(--yellow-a), var(--yellow-b)); }
  .tile--pink   { background: linear-gradient(90deg, var(--pink-a), var(--pink-b)); }
  .tile--pale   { background: linear-gradient(180deg, var(--pale-a), var(--pale-b)); }
  .tile--orange { background: linear-gradient(90deg, var(--orange-a), var(--orange-b)); }
  .tile--brown  { background: linear-gradient(90deg, var(--brown-a), var(--brown-b)); }
  .tile--teal   { background: linear-gradient(90deg, var(--teal-a), var(--teal-b)); }
  .tile--navy   { background: linear-gradient(90deg, var(--navy-a), var(--navy-b)); }

  .tile-label { font-size: 24px; padding: 22px 24px; letter-spacing: .2px; }
  .tile-label--right { margin-left: auto; }
  .tile-label--small { font-size: 13px; padding: 12px 12px; }
  .tile-label--tiny  { font-size: 12px; padding: 10px 10px; }

  .thumb {
    position: absolute;
    background: linear-gradient(180deg, #fafafa, #dcdcdc);
    border: 1px solid #cfcfcf;
    display: flex; flex-direction: column; align-items: center; justify-content: center;
  }
  .thumb-add { font-size: 8px; font-weight: 700; color: var(--add-green); margin-top: 2px; }
  .thumb-add--dark { color: #333; }

  .meta {
    position: absolute;
    color: var(--ink-grey);
    font-weight: 700;
    font-size: 11px;
    line-height: 13px;
  }
  .meta--right { text-align: right; }
  .catalogue-title { font-size: 17px; color: var(--ink-grey); font-weight: 700; }
  .catalogue-slogan { font-size: 10px; font-style: italic; color: var(--ink-grey); font-weight: 700; letter-spacing: .3px; }

  .banner {
    position: absolute;
    left: 17px; top: 16px; width: 272px; height: 50px;
    background: linear-gradient(180deg, #fbfbfb, #dedede);
    border: 1px solid #d0d0d0;
    display: flex; align-items: center; justify-content: center;
    padding-bottom: 6px;
    color: #888; font-weight: 700; font-size: 13px;
  }
</style>
</head>
<body>

<svg class="sprites" aria-hidden="true">
  <defs>
    <symbol id="icon-star" viewBox="0 0 24 24">
      <path d="M12 1.5l3.1 7.1 7.7.7-5.8 5.1 1.7 7.6L12 18l-6.7 4 1.7-7.6L1.2 9.3l7.7-.7z"/>
    </symbol>
    <symbol id="icon-home" viewBox="0 0 24 24">
      <path d="M12 2L1 12h3v10h6v-7h4v7h6V12h3z"/>
    </symbol>
    <symbol id="icon-play" viewBox="0 0 24 24">
      <path d="M5 3l16 9-16 9z"/>
    </symbol>
    <symbol id="icon-gear" viewBox="0 0 24 24">
      <path fill-rule="evenodd" d="M10 1h4l.6 3.1 1.8.8 2.6-1.8 2.9 2.9-1.8 2.6.8 1.8L23 10v4l-3.1.6-.8 1.8 1.8 2.6-2.9 2.9-2.6-1.8-1.8.8L14 23h-4l-.6-3.1-1.8-.8-2.6 1.8-2.9-2.9 1.8-2.6-.8-1.8L1 14v-4l3.1-.6.8-1.8-1.8-2.6 2.9-2.9 2.6 1.8 1.8-.8zM12 8a4 4 0 100 8 4 4 0 000-8z"/>
    </symbol>
  </defs>
</svg>

<!-- Home menu -->
<section class="screen screen--home" aria-label="Home menu">
  <div class="tile tile--green" style="left:30px;top:31px;width:223px;height:111px;"><span class="tile-label">Wallpapers</span></div>
  <div class="tile tile--blue" style="left:253px;top:31px;width:223px;height:111px;"><span class="tile-label tile-label--right">Ringtones</span></div>
  <div class="tile tile--red" style="left:476px;top:31px;width:112px;height:111px;"><svg width="54" height="54" fill="#fff"><use href="#icon-gear"/></svg></div>

  <div class="tile tile--yellow" style="left:30px;top:142px;width:223px;height:113px;"><span class="tile-label" style="padding-top:16px;">Free Games</span></div>
  <div class="tile tile--pink" style="left:253px;top:142px;width:112px;height:113px;"><svg width="62" height="62" fill="#fff"><use href="#icon-star"/></svg></div>
  <div class="tile tile--pale" style="left:365px;top:142px;width:111px;height:113px;"><svg width="62" height="62" fill="#c4c4c4"><use href="#icon-star"/></svg></div>
  <div class="tile tile--orange" style="left:476px;top:142px;width:112px;height:113px;"><svg width="62" height="62" fill="#fff"><use href="#icon-star"/></svg></div>

  <div class="tile tile--brown" style="left:30px;top:255px;width:112px;height:111px;"><svg width="66" height="66" fill="#fff"><use href="#icon-home"/></svg></div>
  <div class="tile tile--teal" style="left:142px;top:255px;width:223px;height:111px;"><span class="tile-label" style="padding-top:15px;padding-left:16px;">Entertainment</span></div>
  <div class="tile tile--navy" style="left:365px;top:255px;width:223px;height:111px;"><span class="tile-label tile-label--right" style="padding-top:15px;">News</span></div>
</section>

<!-- Ringtone detail -->
<section class="screen screen--ringtone" aria-label="Ringtone detail">
  <div class="tile tile--green" style="left:15px;top:17px;width:114px;height:57px;"></div>
  <div class="tile tile--blue" style="left:129px;top:17px;width:114px;height:57px;"><span class="tile-label tile-label--small tile-label--right">Ringtones</span></div>
  <div class="tile tile--red" style="left:243px;top:17px;width:57px;height:57px;"></div>

  <div class="thumb" style="left:15px;top:87px;width:50px;height:50px;"><svg width="30" height="30" fill="var(--icon-grey)"><use href="#icon-star"/></svg></div>
  <div class="thumb" style="left:65px;top:87px;width:51px;height:50px;"><svg width="30" height="30" fill="var(--icon-grey)"><use href="#icon-star"/></svg></div>
  <div class="thumb" style="left:116px;top:87px;width:50px;height:50px;"></div>
  <p class="meta" style="left:178px;top:105px;">Duration - 1 min</p>

  <div class="thumb" style="left:15px;top:139px;width:50px;height:50px;"></div>
  <div class="thumb" style="left:65px;top:139px;width:51px;height:50px;"><svg width="26" height="26" fill="var(--icon-grey)"><use href="#icon-play"/></svg></div>
  <div class="thumb" style="left:116px;top:139px;width:50px;height:50px;"><svg width="26" height="26" fill="var(--icon-grey)"><use href="#icon-play"/></svg></div>
  <div class="thumb" style="left:166px;top:139px;width:52px;height:50px;"><svg width="26" height="26" fill="var(--icon-grey)"><use href="#icon-play"/></svg></div>
  <div class="thumb" style="left:218px;top:139px;width:51px;height:50px;"></div>
</section>

<!-- Wallpaper detail -->
<section class="screen screen--wallpaper" aria-label="Wallpaper detail">
  <div class="tile tile--green" style="left:15px;top:16px;width:114px;height:58px;"><span class="tile-label tile-label--small">Wallpapers</span></div>
  <div class="tile tile--yellow" style="left:15px;top:74px;width:114px;height:57px;"></div>
  <div class="tile tile--brown" style="left:15px;top:131px;width:57px;height:57px;"><svg width="34" height="34" fill="#fff"><use href="#icon-home"/></svg></div>

  <p class="meta meta--right" style="right:13px;top:21px;">Size - 1024*768<br>Theme - Nature</p>

  <div class="thumb" style="left:152px;top:59px;width:73px;height:40px;"><svg width="28" height="28" fill="var(--icon-grey)"><use href="#icon-star"/></svg></div>
  <div class="thumb" style="left:231px;top:59px;width:72px;height:40px;"><svg width="28" height="28" fill="var(--icon-grey)"><use href="#icon-star"/></svg></div>
  <div class="thumb" style="left:152px;top:103px;width:49px;height:50px;"><svg width="28" height="28" fill="var(--icon-grey)"><use href="#icon-star"/></svg><span class="thumb-add">Add</span></div>
  <div class="thumb" style="left:203px;top:103px;width:48px;height:50px;"><svg width="28" height="28" fill="var(--icon-grey)"><use href="#icon-star"/></svg></div>
  <div class="thumb" style="left:253px;top:103px;width:50px;height:50px;"><svg width="28" height="28" fill="var(--icon-grey)"><use href="#icon-star"/></svg></div>
  <div class="thumb" style="left:152px;top:156px;width:73px;height:42px;"><svg width="28" height="28" fill="var(--icon-grey)"><use href="#icon-star"/></svg></div>
  <div class="thumb" style="left:231px;top:156px;width:72px;height:42px;"><svg width="28" height="28" fill="var(--icon-grey)"><use href="#icon-star"/></svg></div>
</section>

<!-- Catalogue welcome -->
<section class="screen screen--catalogue" aria-label="Catalogue welcome">
  <div class="tile tile--green" style="left:15px;top:16px;width:114px;height:58px;"></div>
  <div class="tile tile--blue" style="left:129px;top:16px;width:114px;height:58px;"></div>
  <div class="tile tile--red" style="left:243px;top:16px;width:57px;height:58px;"></div>
  <div class="tile tile--yellow" style="left:15px;top:74px;width:114px;height:57px;"></div>
  <div class="tile tile--brown" style="left:15px;top:131px;width:58px;height:57px;"></div>
  <div class="tile tile--teal" style="left:73px;top:131px;width:113px;height:57px;"></div>

  <div class="meta meta--right" style="right:17px;top:90px;">
    <p class="catalogue-title">Topic of catalogue</p>
    <p class="catalogue-slogan" style="margin-right:8px;">“Slogan text here”</p>
  </div>
</section>

<!-- Free games -->
<section class="screen screen--games" aria-label="Free games">
  <div class="banner">Banner Image</div>
  <div class="tile tile--yellow" style="left:17px;top:74px;width:113px;height:57px;"><span class="tile-label tile-label--tiny">Free Games</span></div>
  <div class="tile tile--brown" style="left:17px;top:131px;width:56px;height:57px;"><svg width="34" height="34" fill="#fff"><use href="#icon-home"/></svg></div>
  <div class="tile tile--teal" style="left:73px;top:131px;width:114px;height:57px;"></div>

  <div class="thumb" style="left:141px;top:78px;width:50px;height:50px;"><svg width="28" height="28" fill="var(--icon-grey)"><use href="#icon-star"/></svg><span class="thumb-add thumb-add--dark">Add</span></div>
  <div class="thumb" style="left:191px;top:78px;width:50px;height:50px;"><svg width="28" height="28" fill="var(--icon-grey)"><use href="#icon-star"/></svg></div>
  <div class="thumb" style="left:242px;top:78px;width:49px;height:50px;"></div>
  <div class="thumb" style="left:191px;top:134px;width:50px;height:52px;"><svg width="28" height="28" fill="var(--icon-grey)"><use href="#icon-star"/></svg></div>
</section>

</body>
</html>
```